TEK Logistics - Banner 2.5' x 8' for 20+ locations

Need a banner designed that will pop. This banner will be displayed at over 20 of our transportation facilities. Goal is for the banner to grab the attention of employees, contractors and clients and help reinforce our mission and core values. Designed needs to include TEK Logo, our core values and mission statement. Red and Black are the main company colors and we need to stay within that theme and color pallet. Attached is a previous version that was too basic and boring. Willing to consider a design that excludes the mission statement.

Gathering more feedback

```html
<!DOCTYPE html>
<html lang="en">
<head>
<meta charset="utf-8">
<title>TEK Logistics – Core Values Banner</title>
<link href="https://fonts.googleapis.com/css2?family=Exo+2:wght@600;700&family=Chewy&display=swap" rel="stylesheet">
<style>
  :root {
    --page-bg: #e4e4e4;
    --banner-black: #2d2a28;
    --brand-red: #d3211b;
    --pill-white: #ffffff;
    --ink: #2d2a28;
  }
  html, body {
    margin: 0;
    padding: 0;
    width: 1200px;
    height: 861px;
    overflow: hidden;
    background: var(--page-bg);
  }
  .banner {
    position: absolute;
    left: 128px;
    top: 287px;
    width: 944px;
    height: 295px;
    display: block;
  }
  .banner-field { fill: var(--banner-black); }
  .connector { stroke: var(--brand-red); stroke-width: 6; fill: none; stroke-linecap: round; }
  .pill-edge { fill: var(--brand-red); }
  .pill-face { fill: var(--pill-white); }
  .value-text {
    font-family: "Exo 2", sans-serif;
    font-weight: 700;
    font-size: 46px;
    fill: var(--ink);
  }
  .brand-name {
    font-family: "Exo 2", sans-serif;
    font-weight: 700;
    fill: var(--pill-white);
  }
  .fun-text {
    font-family: "Chewy", cursive;
    font-size: 44px;
    fill: var(--pill-white);
  }
  .fun-underline { stroke: var(--brand-red); stroke-width: 8; fill: none; stroke-linejoin: miter; }
  .fun-icon { fill: var(--brand-red); }
  .mission-band { fill: var(--brand-red); }
  .mission-chevron { stroke: var(--pill-white); stroke-width: 9; fill: none; }
  .mission-text {
    font-family: "Exo 2", sans-serif;
    font-weight: 700;
    font-size: 34px;
    fill: var(--pill-white);
  }
</style>
</head>
<body>
<svg class="banner" viewBox="0 0 1574 492" xmlns="http://www.w3.org/2000/svg">
  <rect class="banner-field" x="0" y="0" width="1574" height="492"/>

  <!-- brand name -->
  <g class="brand">
    <text class="brand-name" x="65" y="222" font-size="104" textLength="330" lengthAdjust="spacingAndGlyphs">TEK</text>
    <text class="brand-name" x="70" y="276" font-size="42" letter-spacing="8" textLength="325" lengthAdjust="spacingAndGlyphs">LOGISTICS</text>
  </g>

  <!-- connectors -->
  <g class="connectors">
    <polyline class="connector" points="439,122 482,77"/>
    <polyline class="connector" points="460,174 522,152"/>
    <polyline class="connector" points="465,229 529,229"/>
    <polyline class="connector" points="452,277 522,307"/>
    <polyline class="connector" points="425,320 487,384"/>
  </g>

  <!-- core values -->
  <g class="value">
    <path class="pill-edge" d="M500,19 H1447 L1470,52 L1447,85 H490 Z"/>
    <path class="pill-face" d="M502,13 H1437 L1458,46 L1437,79 H482 V33 Q482,13 502,13 Z"/>
    <text class="value-text" x="509" y="61" textLength="918" lengthAdjust="spacingAndGlyphs">Do the right things for the right reasons</text>
  </g>
  <g class="value">
    <path class="pill-edge" d="M540,95 H1376 L1399,128 L1376,161 H530 Z"/>
    <path class="pill-face" d="M542,89 H1366 L1387,122 L1366,155 H522 V109 Q522,89 542,89 Z"/>
    <text class="value-text" x="549" y="137" textLength="730" lengthAdjust="spacingAndGlyphs">Pursue growth and development</text>
  </g>
  <g class="value">
    <path class="pill-edge" d="M547,173 H1318 L1341,206 L1318,239 H537 Z"/>
    <path class="pill-face" d="M549,167 H1308 L1329,200 L1308,233 H529 V187 Q529,167 549,167 Z"/>
    <text class="value-text" x="546" y="215" textLength="757" lengthAdjust="spacingAndGlyphs">Build a positive team atmosphere</text>
  </g>
  <g class="value">
    <path class="pill-edge" d="M540,248 H1242 L1265,281 L1242,314 H530 Z"/>
    <path class="pill-face" d="M542,242 H1232 L1253,275 L1232,308 H522 V262 Q522,242 542,242 Z"/>
    <text class="value-text" x="543" y="290" textLength="675" lengthAdjust="spacingAndGlyphs">Deliver WOW through service</text>
  </g>
  <g class="value">
    <path class="pill-edge" d="M505,325 H1004 L1027,358 L1004,391 H495 Z"/>
    <path class="pill-face" d="M507,319 H994 L1015,352 L994,385 H487 V339 Q487,319 507,319 Z"/>
    <text class="value-text" x="511" y="367" textLength="473" lengthAdjust="spacingAndGlyphs">Do everything Safely</text>
  </g>

  <!-- have fun -->
  <g class="fun">
    <circle class="fun-icon" cx="1427" cy="249" r="57" role="img" aria-label="Smiling face icon"/>
    <text class="fun-text" x="1295" y="362" textLength="232" lengthAdjust="spacingAndGlyphs">Have Fun</text>
    <polyline class="fun-underline" points="1287,380 1534,380 1553,350 1534,320"/>
  </g>

  <!-- mission -->
  <g class="mission">
    <polygon class="mission-band" points="82,402 1494,402 1516,439 1494,476 82,476 60,439"/>
    <polyline class="mission-chevron" points="72,404 50,439 72,474"/>
    <polyline class="mission-chevron" points="1504,404 1526,439 1504,474"/>
    <text class="mission-text" x="156" y="433" textLength="1264" lengthAdjust="spacingAndGlyphs">Provide the best customer experience while creating an environment of</text>
    <text class="mission-text" x="98" y="465" textLength="1380" lengthAdjust="spacingAndGlyphs">growth and opportunity for our customers, employees, and service providers.</text>
  </g>
</svg>
</body>
</html>
```